Guaranteed Job - Sleek Sexy Business Card UV Spot

Im looking for a sleek and sexy business card, that resembles elite or VIP status status.
our business is corinvale.example
you can view our products on there, but our main audience for handing out our cards will be for people in the hospitality industry, so it will need to impress high management and CEO of hotels and restaurants, bars, clubs etc...
the card features will have UV spot on both sides, 400gsm stock. standard size.
Artwork should be 86 x 54mm + 2mm bleed = 90 x 58mm
it should have a nice "unique" uv spot pattern that highlights the card, not a repeated pattern, theres no originality there, and it will be disregarded.
The written material will be:
Corin Vale Hospitality College (logo)
Tobin Marsh
Director
Phone: 1300 615 737
Mobile: 0455 817 296
Email: info@corinvale.example
website: www.corinvale.example
I'm looking for originality here, i don't want just a simple stock card, want something that has a wow factor for people.
You will find the logo attached. you may invert the white to black words to suit the background as you please.
thank you and good luck
As a side note, ive received a lot of proposals, im too busy to give feedback to each and every one, so if i havent provided feedback for your design within 24 hours, then consider it not acceptable, and you could resubmit another design.
So far i have not seen any design that stood out for me, they all seem pretty generic. there nothing thats unique, i would figure for the amount that im offering, that people would put some more effort and creativity into the design.
so far over 200 designs submitted, and nothing i have seen looks very original, everything looks like a different variation of the same stuff, i said it very clearly i wanted something unique, the only thing that has come close to it so far is this one
Reason: Ive received alot of design concepts and i have reviewed everyone, but i havent had time to give feedback to every single one, only the ones that have interested me, if i havent responded, its because i havent found it good enough.
so far only a few design have been on par with what ive been looking for, an attractive eye popping design.
heres a few of them,
http://files.pixelbazaar.example/design_img/51736/62418/62418_2840915_51736_image.jpg
http://files.pixelbazaar.example/design_img/51736/68254/68254_2841377_51736_image.jpg
theyre, both unique and original, and eye catching, the only thing theyre missing is the sexyness.
if you still think you have some creativity left in your minds, then throw it on here.
Reason: Sorry guys for the delay, I was in a serious accident and out of commission for the past few months, I'm just slowly recovering now, please bare with me as i try to attend to this project, it may take me awhile as I have other projects that are on standby, I'm not 100% at the moment, so im extending the deadline for 2 weeks right now. Thanks for your patience.
Hospitality

```html
<!DOCTYPE html>
<html lang="en">
<head>
<meta charset="utf-8">
<title>Corin Vale Hospitality College – Business Card</title>
<link rel="stylesheet" href="https://fonts.googleapis.com/css2?family=Oswald:wght@300;400;500;600&display=swap">
<style>
  :root {
    --backdrop: #8f8f8f;
    --card: #1a1c20;
    --card-deep: #121316;
    --blue: #4a90d0;
    --blue-dark: #1f5596;
    --white: #f2f2f2;
    --muted: #9a9da3;
    --pattern: #2b2d31;
  }
  * { margin: 0; padding: 0; box-sizing: border-box; }
  html, body { width: 1200px; height: 900px; overflow: hidden; }
  body {
    background: var(--backdrop);
    font-family: "Oswald", "Arial Narrow", sans-serif;
    position: relative;
  }
  .card {
    position: absolute;
    top: 280px;
    width: 540px;
    height: 340px;
    border-radius: 4px;
    overflow: hidden;
    box-shadow: 0 10px 24px rgba(0,0,0,0.35);
  }
  /* Contact side */
  .card--contact { left: 40px; background: var(--card); }
  .brand {
    position: absolute;
    top: 34px;
    left: 36px;
    display: flex;
    align-items: center;
    gap: 12px;
  }
  .brand__dot {
    width: 14px; height: 14px;
    background: var(--blue);
  }
  .brand__name {
    color: var(--white);
    font-weight: 500;
    font-size: 22px;
    line-height: 1.1;
    letter-spacing: 0.5px;
    text-transform: uppercase;
  }
  .contact {
    position: absolute;
    left: 330px;
    top: 150px;
  }
  .contact__name {
    color: var(--blue);
    font-weight: 500;
    font-size: 22px;
    letter-spacing: 1px;
    text-transform: uppercase;
  }
  .contact__role {
    color: var(--white);
    font-weight: 300;
    font-size: 14px;
    margin-bottom: 12px;
  }
  .contact__line {
    display: flex;
    align-items: center;
    gap: 10px;
    color: var(--white);
    font-weight: 300;
    font-size: 13px;
    line-height: 22px;
  }
  .contact__line svg { width: 14px; height: 14px; flex: none; }
  .band {
    position: absolute;
    left: 0; bottom: 0;
    width: 540px; height: 90px;
  }
  .band__url {
    position: absolute;
    left: 36px;
    bottom: 52px;
    color: var(--white);
    font-weight: 400;
    font-size: 14px;
    letter-spacing: 0.4px;
  }
  /* Spot-UV side */
  .card--spot {
    left: 620px;
    background: linear-gradient(160deg, var(--card) 0%, var(--card-deep) 100%);
  }
  .spot-pattern {
    position: absolute;
    inset: 0;
    background:
      radial-gradient(circle at 30% 35%, rgba(70,72,78,0.35), transparent 45%),
      radial-gradient(circle at 75% 70%, rgba(70,72,78,0.3), transparent 45%),
      var(--pattern);
    opacity: 0.55;
  }
  .spot-mark {
    position: absolute;
    inset: 0;
    display: flex;
    align-items: center;
    justify-content: center;
    gap: 14px;
  }
  .spot-mark__dot {
    width: 22px; height: 22px;
    border-radius: 50%;
    background: var(--blue);
  }
  .spot-mark__name {
    color: var(--white);
    font-weight: 600;
    font-size: 48px;
    letter-spacing: 2px;
    text-transform: uppercase;
  }
</style>
</head>
<body>

  <section class="card card--contact" aria-label="Business card, contact side">
    <div class="brand">
      <span class="brand__dot"></span>
      <div class="brand__name">Corin Vale<br>Hospitality College</div>
    </div>

    <div class="contact">
      <div class="contact__name">Tobin Marsh</div>
      <div class="contact__role">Director</div>
      <div class="contact__line">
        <svg viewBox="0 0 16 16" aria-hidden="true"><path fill="var(--blue)" d="M3 1l3 3-1.5 2a8 8 0 0 0 5.5 5.5L12 10l3 3-2 2C7 15 1 9 1 3z"/></svg>
        1300 615 737
      </div>
      <div class="contact__line">
        <svg viewBox="0 0 16 16" aria-hidden="true"><rect x="4" y="1" width="8" height="14" rx="1.5" fill="var(--blue)"/><rect x="5.5" y="3" width="5" height="8" fill="var(--card)"/></svg>
        0455 817 296
      </div>
      <div class="contact__line">
        <svg viewBox="0 0 16 16" aria-hidden="true"><rect x="1" y="3" width="14" height="10" fill="var(--blue)"/><path d="M1 3l7 6 7-6" fill="none" stroke="var(--card)" stroke-width="1.4"/></svg>
        info@corinvale.example
      </div>
    </div>

    <svg class="band" viewBox="0 0 540 90" preserveAspectRatio="none" aria-hidden="true">
      <defs>
        <linearGradient id="bandFill" x1="0" y1="0" x2="1" y2="0">
          <stop offset="0" stop-color="var(--blue-dark)"/>
          <stop offset="1" stop-color="var(--blue)"/>
        </linearGradient>
      </defs>
      <path d="M0 0 H300 L312 14 H330 V90 H0 Z" fill="url(#bandFill)"/>
    </svg>
    <div class="band__url">www.corinvale.example</div>
  </section>

  <section class="card card--spot" aria-label="Business card, spot UV side">
    <div class="spot-pattern" role="img" aria-label="Spot UV illustration of scattered cocktail glasses, wine glasses, citrus slices and cherries"></div>
    <div class="spot-mark">
      <span class="spot-mark__dot"></span>
      <span class="spot-mark__name">Corin Vale</span>
    </div>
  </section>

</body>
</html>
```